Dental promotion

We are a family dental office that provides 99% of the dental service for the entire family, including IV sedation, wisdom teeth extraction, implant, Trelaform, root canal, teeth whiting et cl. We currently have promotion for Trelaform, implant and new patients who don’t have insurance. 1500 off Trelaform, 2000 off for implant, 98 dollars for new patient that cover exam, x-ray, and regular cleaning. We also offer financing option.
More information please check our website
https://www.quellmoorfamilydentistry.com/

```html
<!DOCTYPE html>
<html lang="en">
<head>
<meta charset="utf-8">
<title>Quellmoor Family Dentistry – Postcard Back</title>
<link href="https://fonts.googleapis.com/css2?family=Montserrat+Alternates:ital,wght@0,400;0,700;1,700&family=Roboto:wght@500;700&display=swap" rel="stylesheet">
<style>
  :root {
    --brand-purple: #3d3f91;
    --brand-purple-light: #4a4ca6;
    --brand-green: #5aa844;
    --ink: #1d1d22;
    --panel-grey: #e4e9ef;
    --paper: #ffffff;
    --rule: #333333;
  }
  * { margin: 0; padding: 0; box-sizing: border-box; }
  html, body { width: 1200px; height: 920px; overflow: hidden; background: var(--paper); }
  .postcard {
    position: relative;
    width: 1200px; height: 920px;
    background: var(--paper);
    font-family: "Montserrat Alternates", sans-serif;
    color: var(--ink);
  }
  .doctor-band {
    position: absolute; left: 0; top: 70px;
    width: 430px; height: 53px;
    background: linear-gradient(90deg, var(--brand-purple), var(--brand-purple-light));
    color: #fff;
    padding-left: 55px;
    display: flex; align-items: center;
  }
  .doctor-name { font-family: "Roboto", sans-serif; font-weight: 700; font-size: 36px; letter-spacing: 0.2px; }
  .doctor-credentials { font-family: "Roboto", sans-serif; font-weight: 500; font-size: 21px; margin-left: 8px; margin-top: 8px; }
  .doctor-portrait {
    position: absolute; left: 378px; top: 44px;
    width: 268px; height: 268px; border-radius: 50%;
    border: 3px solid var(--brand-green);
    background: var(--paper);
  }
  .doctor-portrait-fill {
    position: absolute; left: 10px; top: 10px;
    width: 242px; height: 242px; border-radius: 50%;
    background: radial-gradient(circle at 50% 40%, #d9c2ad 0%, #b9aa9b 45%, #3a3f6b 100%);
  }
  .doctor-bio {
    position: absolute; left: 55px; top: 146px;
    font-size: 22px; line-height: 31.2px;
  }
  .mission-panel {
    position: absolute; left: 52px; top: 515px;
    width: 532px; height: 230px;
    background: var(--panel-grey);
    overflow: hidden;
  }
  .mission-photo {
    position: absolute; right: 0; top: 0;
    width: 290px; height: 230px;
    background: linear-gradient(90deg, var(--panel-grey) 0%, #e9e4e4 25%, #d9b49b 60%, #c79a83 80%, #e6c4d0 100%);
  }
  .mission-text {
    position: absolute; left: 19px; top: 20px;
    font-weight: 700; font-style: italic;
    font-size: 21px; line-height: 31.2px;
  }
  .financing-pill {
    position: absolute; left: 58px; top: 765px;
    width: 445px; height: 45px; border-radius: 22px;
    background: linear-gradient(90deg, var(--brand-purple), var(--brand-purple-light));
    color: #fff;
    font-family: "Roboto", sans-serif; font-weight: 700;
    font-size: 27px;
    display: flex; align-items: center; justify-content: center;
  }
  .financing-note {
    position: absolute; left: 69px; top: 823px;
    font-size: 22px;
  }
  .practice-mark {
    position: absolute; left: 700px; top: 52px;
    display: flex; align-items: center; gap: 10px;
  }
  .practice-dot { width: 60px; height: 60px; border-radius: 50%; background: var(--brand-green); flex: none; }
  .practice-name {
    font-size: 16px; font-weight: 700; color: var(--brand-purple);
    line-height: 23px; letter-spacing: 1px;
  }
  .practice-address {
    position: absolute; left: 705px; top: 145px;
    font-size: 18px; line-height: 27px;
  }
  .stamp-box {
    position: absolute; left: 1011px; top: 45px;
    width: 158px; height: 167px;
    border: 1px solid var(--rule);
  }
  .mailing-line {
    position: absolute; left: 748px; width: 387px;
    border-top: 1px solid var(--rule);
  }
  .mailing-line--first { top: 425px; }
  .mailing-line--second { top: 519px; }
  .mailing-line--third { top: 612px; }
</style>
</head>
<body>
<div class="postcard">
  <div class="doctor-band">
    <span class="doctor-name">DR. VELLER,</span>
    <span class="doctor-credentials">D.D.S. Ph.D.</span>
  </div>
  <div class="doctor-portrait">
    <div class="doctor-portrait-fill" role="img" aria-label="Portrait photo of Dr. Veller"></div>
  </div>
  <p class="doctor-bio">
    Dr. Veller keeps up with<br>
    the latest advances in<br>
    dentistry by attending<br>
    continuing education<br>
    courses and takes pride<br>
    in offering state-of-the-<br>
    art quality dental care with a<br>
    gentle touch. When Dr. Veller is not creating<br>
    life-changing smiles at his practice, he enjoys<br>
    spending time with his wife and two sons<br>
    engaging in outdoor activities.
  </p>

  <div class="mission-panel">
    <div class="mission-photo" role="img" aria-label="Photo of a smiling patient in the dental chair during a check-up"></div>
    <p class="mission-text">
      Provide superior<br>
      family and cosmetic<br>
      dental care in a<br>
      friendly, comfortable,<br>
      modern, and safe<br>
      environment.
    </p>
  </div>

  <div class="financing-pill">WE OFFER FINANCING OPTION</div>
  <p class="financing-note">More information please call or visit us</p>

  <div class="practice-mark">
    <span class="practice-dot"></span>
    <span class="practice-name">QUELLMOOR<br>FAMILY DENTISTRY</span>
  </div>
  <p class="practice-address">
    4270 Marrowfield Lane, Suite<br>
    #205 Raleigh, NC 27615
  </p>

  <div class="stamp-box"></div>
  <div class="mailing-line mailing-line--first"></div>
  <div class="mailing-line mailing-line--second"></div>
  <div class="mailing-line mailing-line--third"></div>
</div>
</body>
</html>
```